Willow Crest Website

We need a website that has clean, asian looking images that relax and motivate people to come into our integrated medical center. My current website is www.pinebrookcare.example and I would like the design for Willow Crest Health Solutions to be similar but more inviting with video content and a product purchase store as well. A moving banner would be nice too. When people are looking for ways of losing weight or getting out of pain we want them to make the connection that we have the solution. This website needs to provide sufficient information so that patients are well informed and choose us as their health provider before they ever walk through our doors. We offer comprehensive natural medicine that is based on the principles that the body can heal itself when given the right conditions. Our services include medical weight loss and hormone balancing, acupuncture and chinese herbal medicine, physical medicine, trigger point injections, allergy testing and joint rehabilitation. The Medical Doctor and Licensed Acupuncturist work as a team to provide optimal care that is catered to each individual who comes through our doors.
Updates

Target Market(s)

40 to 50 year olds who want to lose weight or have pain issues.

Industry/Entity Type

Medical

Requirements
Must have
• Use photos from our website www.pinebrookcare.example or similar content. Video content. Moving banner with relaxing images.
Nice to have
• Happy, healthy looking people. Medical Doctors working as a team. Friendly staff in a cutting edge facility.
Should not have
• Papyrus font, or big bold words.

```html
<!DOCTYPE html>
<html lang="en">
<head>
<meta charset="utf-8">
<title>Willow Crest Health Solutions</title>
<link rel="stylesheet" href="https://fonts.googleapis.com/css2?family=Arimo:wght@400;700&family=Marcellus&display=swap">
<style>
:root{
  --olive:#5d5a22;
  --olive-deep:#3f3d20;
  --olive-line:#7a7636;
  --cream:#f4f3ee;
  --card-line:#dcdcd4;
  --green:#5aa21a;
  --green-top:#8ccf3a;
  --orange:#f7941d;
  --orange-deep:#e67c0b;
  --khaki:#c8bf86;
  --khaki-deep:#a79d5e;
  --khaki-dark:#6b6530;
  --footer:#a3a291;
  --text:#444;
  --white:#fff;
}
*{box-sizing:border-box;margin:0;padding:0}
html,body{width:1017px;height:1200px;overflow:hidden;background:var(--white)}
body{position:relative;font-family:"Arimo",Arial,sans-serif;color:var(--text)}
.abs{position:absolute}

/* header */
.sidebar{left:0;top:0;width:244px;height:370px;background:var(--olive)}
.brand{left:40px;top:22px;width:164px;text-align:center;color:var(--white);font-size:20px;letter-spacing:1px;display:flex;flex-direction:column;align-items:center;gap:10px}
.brand-mark{width:18px;height:18px;background:var(--white)}
.services{left:26px;top:158px;list-style:none}
.services li{color:var(--white);font-weight:700;font-size:13.3px;height:24.4px;display:flex;align-items:center;letter-spacing:.2px;white-space:nowrap}
.services li::before{content:"";width:9px;height:9px;border-radius:50%;background:var(--white);margin-right:8px;box-shadow:inset 0 0 0 2px #ddd}
.banner{left:244px;top:0;width:773px;height:370px;background:linear-gradient(120deg,#e9d3c4 0%,#f4e6dc 40%,#e7c8b5 70%,#f2e4da 100%)}
.arrow{top:105px;width:26px;height:120px;background:rgba(120,120,120,.55)}
.arrow.prev{left:244px;border-radius:0 60px 60px 0}
.arrow.next{left:991px;border-radius:60px 0 0 60px}
.arrow svg{position:absolute;top:50px;left:6px}
.promo{top:296px;height:72px;border-radius:6px;background:linear-gradient(var(--green-top),var(--green));border:2px solid #4b8c14;color:var(--white);font-weight:700;font-size:14px;line-height:24px;padding:12px 10px 12px 22px;letter-spacing:.2px;white-space:nowrap}
.promo.tight{padding-left:13px;padding-right:6px}
.promo .icon{position:absolute;right:12px;top:-22px;width:50px;height:56px;border-radius:50%}

/* info band */
.info{left:0;top:370px;width:1017px;height:305px;background:var(--olive-deep)}
.info h1{position:absolute;left:15px;top:10px;font-family:"Marcellus",Georgia,serif;font-weight:400;font-size:20px;color:var(--white);letter-spacing:.5px}
.info .copy{position:absolute;left:16px;top:41px;width:674px;color:#eeeadb;font-size:11.8px;line-height:14.7px}
.info .copy p{margin-bottom:14.7px}
.video{left:703px;top:415px;width:298px;height:198px;background:linear-gradient(100deg,#c99a83,#8e6a5a 45%,#3a3430 75%,#26221f)}
.play{left:808px;top:469px}
.all-videos{left:900px;top:632px;color:var(--white);font-weight:700;font-size:11.5px}

/* shop */
.shop{left:0;top:675px;width:1017px;height:455px;background:var(--cream)}
.shop-side{left:0;top:675px;width:195px;height:455px;background:#f6f5f0;border-right:2px solid #e3e2da}
.search{left:10px;top:706px;width:193px;height:68px;background:linear-gradient(var(--orange),var(--orange-deep));border-radius:3px 3px 0 3px}
.search .field{position:absolute;left:14px;top:22px;width:168px;height:22px;background:var(--white);border:1px solid #d27010}
.search .field svg{position:absolute;left:6px;top:4px}
.cart{left:15px;top:799px;width:168px;height:169px;border-radius:8px;background:linear-gradient(#e3dcb4,var(--khaki));border:1px solid var(--khaki-deep)}
.cart h2{position:absolute;left:14px;top:10px;font-size:12px;color:#555;font-weight:700}
.cart .empty{position:absolute;left:15px;top:34px;font-size:12px;color:var(--white);font-weight:700}
.cart .row{position:absolute;left:12px;width:142px;height:21px;background:var(--khaki-deep);color:var(--white);font-size:12px;font-weight:700;display:flex;justify-content:space-between;align-items:center;padding:0 6px}
.checkout{position:absolute;left:84px;top:131px;width:74px;height:22px;background:var(--khaki-dark);color:var(--white);font-size:12px;font-weight:700;display:flex;align-items:center;justify-content:center}
.specials-title{left:28px;top:995px;font-size:12px;font-weight:700;color:#555}
.special-img{left:40px;top:1028px;width:38px;height:70px;background:linear-gradient(#333,#c7c21a 60%,#333);border-radius:4px}
.special-name{left:95px;top:1033px;color:var(--orange);font-weight:700;font-size:14px}
.special-old{left:95px;top:1061px;font-size:11px;color:#777;text-decoration:line-through}
.special-new{left:95px;top:1083px;font-size:13px;font-weight:700;color:#444}

.card{width:250px;height:137px;background:var(--white);border:1px solid var(--card-line);border-radius:3px}
.card .pic{position:absolute;left:8px;top:12px;width:56px;height:80px;border-radius:4px}
.card h3{position:absolute;left:75px;top:14px;color:var(--orange);font-size:14px;font-weight:700}
.card p{position:absolute;left:77px;top:39px;width:168px;font-size:10.6px;line-height:13px;color:#444}
.card .btn{position:absolute;top:96px;width:76px;height:21px;border-radius:11px;font-size:10.6px;display:flex;align-items:center;justify-content:center}
.card .details{left:79px;background:linear-gradient(#fafafa,#ddd);border:1px solid #c8c8c8;color:#555}
.card .add{left:169px;background:linear-gradient(#dcd4a4,#b9ae70);border:1px solid #a79d5e;color:#555}

/* footer */
.footer{left:0;top:1130px;width:1017px;height:70px;background:var(--footer)}
.legal{left:22px;top:1160px;font-size:10px;color:#f4eec6}
.legal span{margin:0 8px;color:#e0dab0}
.copyright{left:620px;top:1163px;font-size:10.6px;color:#6f6b44}
.social{top:1148px;width:33px;height:33px;border-radius:5px;background:#8b8a7a}
</style>
</head>
<body>

<!-- header -->
<div class="abs sidebar"></div>
<div class="abs brand"><span class="brand-mark"></span>Willow Crest</div>
<ul class="abs services">
  <li>MEDICAL WEIGHT LOSS</li>
  <li>HORMONE BALANCING</li>
  <li>ACUPUNCTURE</li>
  <li>CHINESE HERBAL MEDICINE</li>
  <li>PHYSICAL MEDICINE</li>
  <li>TRIGGER POINT INJECTIONS</li>
  <li>ALLERGY TESTING</li>
  <li>JOINT REHABILITATION</li>
</ul>
<div class="abs banner" role="img" aria-label="Rotating banner photo: acupuncture needles placed on a relaxed patient's forehead"></div>
<div class="abs arrow prev"><svg width="12" height="20" viewBox="0 0 12 20"><path d="M11 0 L0 10 L11 20 Z" fill="#fff"/></svg></div>
<div class="abs arrow next"><svg width="12" height="20" viewBox="0 0 12 20"><path d="M1 0 L12 10 L1 20 Z" fill="#fff"/></svg></div>

<div class="abs promo" style="left:247px;width:273px">BEST DIET ADVICE<br>YOU'VE NEVER HEARD
  <span class="icon" role="img" aria-label="Pear illustration" style="background:radial-gradient(#d8d25a,#8c8a1e)"></span></div>
<div class="abs promo tight" style="left:522px;width:218px">OUR FASTEST<br>WEIGHT LOSS PROGRAMS
  <span class="icon" role="img" aria-label="Speed gauge illustration" style="right:22px;background:radial-gradient(#555,#222);border:3px solid #ccc"></span></div>
<div class="abs promo" style="left:742px;width:274px">EXERCISE AND<br>PHYSICAL FITNESS
  <span class="icon" role="img" aria-label="Dumbbell illustration" style="width:60px;background:radial-gradient(#eee,#999)"></span></div>

<!-- info -->
<section class="abs info">
  <h1>HOW DOES ACUPUNCTURE WORK?</h1>
  <div class="copy">
    <p>As the needles are carefully inserted into acupuncture points, specific cells stimulate nerve pathways that trigger a healing response to a particular organ system or area of the body.&nbsp; Acupuncture also acts on the autonomic nervous system and causes the release of endorphins, enkephalins and other natural pain relieving chemicals.&nbsp; At Willow Crest Acupuncture the system of acupuncture used is called Seitai Shinpo (which translates into “correct posture acupuncture method”) that uses acupuncture and moxibustion to balance structural distortions by releasing tense areas of contraction along the spine. When the structure is properly balanced then the body will heal much quicker.</p>
    <p>Acupuncture has been used to effectively treat numerous health conditions for thousands of years.&nbsp; According to the World Health Organization, ¼ of the earth’s population receives acupuncture treatment on a continual basis.&nbsp; Both the WHO and the National Institutes of Health endorse acupuncture for many common problems.</p>
    <p>Acupuncture needles are engineered so precisely that usually a very mild sensation is felt, if any at all.&nbsp; The needles are about the diameter of a hair.&nbsp; Most patients report feeling deeply relaxed and often have instant pain relief.</p>
    <p>There are very few adverse reactions to acupuncture but in some cases your condition may temporarily exacerbated following the treatment.&nbsp; This is a sign of detoxification and is considered to be a good thing.&nbsp; Soaking your feet in Epsom salts and hot water and getting in plenty of fluids and nutrition will ease the process.</p>
  </div>
</section>
<div class="abs video" role="img" aria-label="Video still: practitioner's hand placing acupuncture needles on a patient's back"></div>
<svg class="abs play" width="94" height="94" viewBox="0 0 94 94" aria-hidden="true">
  <circle cx="47" cy="47" r="45" fill="#9a9a9a" opacity=".85"/>
  <circle cx="47" cy="47" r="37" fill="#3a3a3a"/>
  <path d="M36 28 L66 47 L36 66 Z" fill="#e8e8e8"/>
</svg>
<div class="abs all-videos">VIEW ALL VIDEOS</div>

<!-- shop -->
<div class="abs shop"></div>
<div class="abs shop-side"></div>
<div class="abs search"><div class="field"><svg width="14" height="14" viewBox="0 0 14 14"><circle cx="5.5" cy="5.5" r="4" fill="none" stroke="#555" stroke-width="2"/><path d="M8.5 8.5 L13 13" stroke="#555" stroke-width="2.4"/></svg></div></div>
<div class="abs cart">
  <h2>CART</h2>
  <div class="empty">No products</div>
  <div class="row" style="top:65px"><span>Shipping</span><span>$0.00</span></div>
  <div class="row" style="top:96px"><span>Total</span><span>$0.00</span></div>
  <div class="checkout">Checkout</div>
</div>
<div class="abs specials-title">SPECIALS</div>
<div class="abs special-img" role="img" aria-label="Supplement bottle"></div>
<div class="abs special-name">Leanwave</div>
<div class="abs special-old">$37.00</div>
<div class="abs special-new">$35.15</div>

<div class="abs card" style="left:222px;top:697px"><div class="pic" role="img" aria-label="Supplement tub" style="background:linear-gradient(#eee,#1c2a4a 40%,#1c2a4a)"></div><h3>Leanwave</h3><p>It is an all-natural, 3-step diet aid with separate “drinks” for the morning, evening, and nighttime.</p><span class="btn details">Details</span><span class="btn add">Add to Cart</span></div>
<div class="abs card" style="left:488px;top:697px"><div class="pic" role="img" aria-label="Supplement tub" style="background:linear-gradient(#2a2550,#463f86)"></div><h3>Leanwave</h3><p>It is an all-natural, 3-step diet aid with separate “drinks” for the morning, evening, and nighttime.</p><span class="btn details">Details</span><span class="btn add">Add to Cart</span></div>
<div class="abs card" style="left:753px;top:697px"><div class="pic" role="img" aria-label="Supplement box" style="width:62px;background:linear-gradient(90deg,#e8e8ec,#c9c9d4)"></div><h3>Leanwave</h3><p>It is an all-natural, 3-step diet aid with separate “drinks” for the morning, evening, and nighttime.</p><span class="btn details">Details</span><span class="btn add">Add to Cart</span></div>

<div class="abs card" style="left:222px;top:842px"><div class="pic" role="img" aria-label="Supplement bottle" style="left:14px;width:40px;background:linear-gradient(#333,#c7c21a 60%,#333)"></div><h3>Leanwave</h3><p>It is an all-natural, 3-step diet aid with separate “drinks” for the morning, evening, and nighttime.</p><span class="btn details">Details</span><span class="btn add">Add to Cart</span></div>
<div class="abs card" style="left:488px;top:842px"><div class="pic" role="img" aria-label="Supplement pack" style="top:22px;width:62px;height:40px;background:linear-gradient(90deg,#ddd,#555)"></div><h3>Leanwave</h3><p>It is an all-natural, 3-step diet aid with separate “drinks” for the morning, evening, and nighttime.</p><span class="btn details">Details</span><span class="btn add">Add to Cart</span></div>
<div class="abs card" style="left:753px;top:842px"><div class="pic" role="img" aria-label="Supplement bottle" style="left:14px;width:44px;background:linear-gradient(#eee,#f28c28 55%,#eee)"></div><h3>Leanwave</h3><p>It is an all-natural, 3-step diet aid with separate “drinks” for the morning, evening, and nighttime.</p><span class="btn details">Details</span><span class="btn add">Add to Cart</span></div>

<div class="abs card" style="left:222px;top:988px"><div class="pic" role="img" aria-label="Liquid supplement bottle" style="background:linear-gradient(#f0f0f0,#dde4ee 50%,#2a3b6a)"></div><h3>Leanwave</h3><p>It is an all-natural, 3-step diet aid with separate “drinks” for the morning, evening, and nighttime.</p><span class="btn details">Details</span><span class="btn add">Add to Cart</span></div>
<div class="abs card" style="left:488px;top:988px"><div class="pic" role="img" aria-label="Green drink in a glass" style="width:62px;background:linear-gradient(#f4f7ea,#b8d640 60%,#5c8a2a)"></div><h3>Leanwave</h3><p>It is an all-natural, 3-step diet aid with separate “drinks” for the morning, evening, and nighttime.</p><span class="btn details">Details</span><span class="btn add">Add to Cart</span></div>
<div class="abs card" style="left:753px;top:988px"><div class="pic" role="img" aria-label="Diet aid box" style="width:62px;background:linear-gradient(90deg,#f4f4f4,#e05a8a)"></div><h3>Leanwave</h3><p>It is an all-natural, 3-step diet aid with separate “drinks” for the morning, evening, and nighttime.</p><span class="btn details">Details</span><span class="btn add">Add to Cart</span></div>

<!-- footer -->
<div class="abs footer"></div>
<div class="abs legal">Privacy Policy<span>|</span>Terms &amp; Conditions<span>|</span>Sitemap</div>
<div class="abs copyright">© 2012 Willow Crest Acupuncture. All Rights Reserved.</div>
<div class="abs social" style="left:917px" role="img" aria-label="Social network link"></div>
<div class="abs social" style="left:962px" role="img" aria-label="Social network link"></div>

</body>
</html>
```